Awesome, colorful pamphlet advertising services for disabled people and supporters

My business, The Ability Crossroads, provides nutritional counseling services to people with and without disabilities throughout the lifespan. It also offers disability consulting, body image coaching and accessible recreation consultation. I would like something representing both children and adults which ties these activities together in a happy way.

Font styles to use
Sans Serif

Colors
00AB8E
00BBA5
67D7C9
C6EFE9
E9F9F6
FFF300
FFF600
FEFA6F
FFFEC7
FFFEE8
F0912C
F2A743
F7CA91
FBE8D2
FDF5EE
E54698
E96AAD
F1A4CE
F9D9EA
FCEFF6
6B429C
8869AF
B7A5CE
E3DAEB
F3F0F8

```html
<!DOCTYPE html>
<html lang="en">
<head>
<meta charset="utf-8">
<title>The Ability Crossroads – Services Pamphlet</title>
<link href="https://fonts.googleapis.com/css2?family=Inter:wght@400;700&display=swap" rel="stylesheet">
<style>
  :root{
    --violet:#5227f5;
    --orange:#f7820f;
    --pink:#e54698;
    --lavender:#8869af;
    --green:#3bd67a;
    --ink:#111111;
    --paper:#ffffff;
    --cream:#fdf5ee;
  }
  *{margin:0;padding:0;box-sizing:border-box}
  html,body{width:1200px;height:848px;overflow:hidden;background:var(--paper)}
  body{font-family:"Inter",Arial,sans-serif;color:var(--ink)}
  .pamphlet{position:relative;width:1200px;height:848px;overflow:hidden}
  .backdrop{position:absolute;inset:0}
  .block{position:absolute}
  h1,h2{font-weight:700;letter-spacing:-0.4px}
  .founder-title{left:0;top:28px;width:404px;text-align:center;font-size:21px;line-height:29px}
  .credentials{left:29px;top:317px;width:360px;list-style:none;color:var(--paper);font-size:15.5px;line-height:28.5px}
  .credentials li,.org-services li,.topics li{position:relative;padding-left:25px}
  .credentials li::before,.org-services li::before,.topics li::before{content:"•";position:absolute;left:0;font-size:11px}
  .founder-quote{left:28px;top:566px;width:360px;color:var(--paper);font-size:15.5px;line-height:24.2px}
  .founder-quote p+p{margin-top:16px}
  .intro{left:432px;top:25px;width:350px;color:var(--cream);font-size:16.5px;line-height:27px}
  .intro p+p{margin-top:27px}
  .org-heading{left:432px;top:578px;font-size:21px}
  .org-services{left:432px;top:619px;width:350px;list-style:none;font-size:15.5px;line-height:28.5px}
  .topics-heading{left:836px;top:28px;width:360px;font-size:22px;line-height:29px;font-weight:400;letter-spacing:-0.2px}
  .topics{left:835px;top:96px;width:360px;list-style:none;font-size:15.5px;line-height:27.1px}
</style>
</head>
<body>
<div class="pamphlet">
  <svg class="backdrop" width="1200" height="848" viewBox="0 0 1200 848">
    <defs>
      <linearGradient id="portraitTone" x1="0" y1="0" x2="0" y2="1">
        <stop offset="0" stop-color="#8a5a3c"/>
        <stop offset="0.45" stop-color="#e8b49a"/>
        <stop offset="1" stop-color="#e7c9c6"/>
      </linearGradient>
      <linearGradient id="rainbowTone" x1="0" y1="0" x2="0" y2="1">
        <stop offset="0" stop-color="#3f6e8f"/>
        <stop offset="0.4" stop-color="#9fb0a0"/>
        <stop offset="0.7" stop-color="#b8642a"/>
        <stop offset="1" stop-color="#3a2418"/>
      </linearGradient>
      <linearGradient id="stageTone" x1="0" y1="0" x2="1" y2="1">
        <stop offset="0" stop-color="#2a1a8a"/>
        <stop offset="0.5" stop-color="#6a1fb0"/>
        <stop offset="1" stop-color="#d33fbd"/>
      </linearGradient>
    </defs>

    <rect x="102" y="98" width="214" height="190" rx="90" fill="url(#portraitTone)" role="img" aria-label="Portrait photo of founder Dana Whitford"/>
    <polygon points="0,264 404,289 404,848 0,848" fill="var(--violet)"/>
    <polygon points="290,290 404,273 404,278" fill="var(--orange)"/>
    <polygon points="300,290 404,279 404,284" fill="var(--pink)"/>
    <polygon points="310,290 404,285 404,289" fill="var(--lavender)"/>
    <polygon points="330,292 404,289 404,301" fill="var(--green)"/>

    <polygon points="404,0 808,0 808,335 404,304" fill="var(--orange)"/>
    <polygon points="404,304 808,335 808,571 404,537" fill="url(#rainbowTone)" role="img" aria-label="Photo of a wooden boardwalk under a rainbow at sunset"/>

    <polygon points="808,616 1200,662 1200,848 808,848" fill="url(#stageTone)" role="img" aria-label="Photo of a microphone on a stage with glowing lights"/>
    <polygon points="1108,651 1200,638 1200,643" fill="var(--orange)"/>
    <polygon points="1118,652 1200,644 1200,649" fill="var(--pink)"/>
    <polygon points="1128,653 1200,650 1200,654" fill="var(--lavender)"/>
    <polygon points="1140,655 1200,654 1200,662" fill="var(--green)"/>
  </svg>

  <h1 class="block founder-title">Meet Dana Whitford - Founder<br>The Ability Crossroads</h1>

  <ul class="block credentials">
    <li>Certified Body Image Coach</li>
    <li>Functional Nutrition &amp; Lifestyle Practitioner</li>
    <li>Certified Functional Nutrition Counselor</li>
    <li>Songsprout Teacher - 4 Levels of Training - Ages 2 Months to 7 Years</li>
    <li>TalkRound Group Facilitator</li>
    <li>Certified Adaptive Recreation &amp; Sports Specialist</li>
  </ul>

  <div class="block founder-quote">
    <p>“As a POTS (Postural Orthostatic Tachycardia Syndrome) patient myself, I fully understand &amp; appreciate the challenges faced by the wider chronic illness community. I am passionate about helping alleviate the pain &amp; suffering associated with POTS &amp; other chronic illnesses &amp; disabilities.</p>
    <p>With over 20 years of experience &amp; relevant qualifications, I am equipped to deliver a range of services effectively.” - Dana Whitford</p>
  </div>

  <div class="block intro">
    <p>Apart from offering nutritional counseling services to people with and without disabilities throughout their lifespan, The Ability Crossroads also offers disability consulting, body image coaching, &amp; accessible recreation consultation to children, adults, &amp; organizations.</p>
    <p>Browse through my services to see how I can help:</p>
  </div>

  <h2 class="block org-heading">Services For Organizations</h2>
  <ul class="block org-services">
    <li>Program development &amp; growth support</li>
    <li>Curriculum &amp; resource creation services based on your goals</li>
    <li>Articles, blog posts &amp; other content on commission</li>
    <li>Handmade collage art &amp; creative writing pieces for your office/program</li>
  </ul>

  <h2 class="block topics-heading">Customized Presentations on the Following Topics:</h2>
  <ul class="block topics">
    <li>Disability history &amp; culture</li>
    <li>Body esteem &amp; eating disorders as a disability issue</li>
    <li>How to build self-definition &amp; self-compassion</li>
    <li>Trauma &amp; disability:<br>What to know &amp; what to do</li>
    <li>Lessons from Disability History:<br>How to embrace our community’s darkest times to create change and healing</li>
    <li>Patient Lifts:<br>What to know and how to incorporate them in a way that works for disabled people</li>
    <li>We are strong:<br>Program Development from a disability rights perspective</li>
    <li>Trauma Response:<br>Helping people ground themselves, stabilize, and recover</li>
  </ul>
</div>
</body>
</html>
```